Awsome new website

We are a Fencing Contracting company in Melbourne Australia. We supply and install Timer and Steel boundary fences as well as Pool fencing (e.g. glass, tubular steel). We also manufacture and install swing and sliding gates.

We want a new website that is a modern business website.
We are targeting domestic and business clients.
The design should compliment our logo and company name.
The website needs to be easy to update.

Some specifics we want.
Menu - Main menu at top of page and smaller footer menu (to add different menu items)
Slider - Main page to have a slider on it that's easy for us to add and remove slides.
Call to action - all pages to have a "call to action" logo or icon that attracts attention (see file "call_to_action.pdf)
Instant quote - we have a online quote page we need a distinctive logo or icon to redirect to this page.
Main page to have a product /Service guide (see file "website_idea.jpg")
Main page to have widgets or quick link to
o why choose us
o Brochures
o Gallery

Have a Gallery page formatted with different category galleries. e.g. Timber, Glass, Feature
Maintain the current link to our staff page with password, (link in footer menu)

Hopefully that covers everything.
Our current website is www.tallowcreekrails.com.au to have a look at the current site.
regards Doug

• Turn off blogging as we don’t want 100’s of comments from spammers to delete

We would like to implement the QX-Portal plugin (see "http://qx-portal-demo.net/" ), but this can be done after the new Theme has been implemented.

```html
<!DOCTYPE html>
<html lang="en">
<head>
<meta charset="utf-8">
<title>Tallow Creek Rails</title>
<link href="https://fonts.googleapis.com/css2?family=PT+Sans+Narrow:wght@400;700&family=Source+Sans+3:wght@400;600;700&display=swap" rel="stylesheet">
<style>
:root{
  --red:#a5141a;
  --red-dark:#7d0d11;
  --red-bright:#c81e22;
  --gold:#f7b733;
  --ink:#3a3a3a;
  --muted:#777;
  --line:#d9d9d9;
  --panel:#f4f4f4;
  --band:#f1f1f1;
  --footer:#2b2b2b;
}
*{margin:0;padding:0;box-sizing:border-box}
html,body{width:979px;height:1200px;overflow:hidden;background:#fff}
body{font-family:"Source Sans 3",sans-serif;color:var(--ink)}
.page{position:relative;width:979px;height:1200px;overflow:hidden}
.abs{position:absolute}

.brand{left:81px;top:14px;width:186px;height:71px;background:var(--red);display:flex;align-items:center;justify-content:center;gap:7px;padding:0 8px}
.brand span{font-family:"Source Sans 3",sans-serif;font-weight:700;font-size:19px;color:#fff;line-height:1;white-space:nowrap}
.brand i{width:10px;height:10px;background:#fff;display:block;flex:none}

.call-badge{left:760px;top:34px;width:144px;height:68px}

.nav{left:0;top:99px;width:979px;height:40px;background:linear-gradient(#b51a1f,#8e1015);border-bottom:3px solid #1d1d1d}
.nav ul{position:absolute;left:82px;top:0;display:flex;list-style:none;height:37px}
.nav li{font-family:"PT Sans Narrow",sans-serif;font-weight:700;font-size:14px;color:#fff;padding:0 19px;line-height:37px;border-right:1px solid #6e0a0e}
.nav li.active{background:#7e0c10;border-left:1px solid #6e0a0e}
.nav .phone{position:absolute;right:82px;top:0;line-height:37px;font-family:"PT Sans Narrow",sans-serif;font-weight:700;font-size:21px;color:var(--gold)}

.slide{left:81px;top:151px;width:817px;height:307px;border-radius:3px;background:linear-gradient(180deg,#7d8d3a 0%,#9aa84a 35%,#8a8f55 62%,#8d8a80 100%)}
.caption{left:0;top:476px;width:979px;text-align:center;font-family:"PT Sans Narrow",sans-serif;font-size:21px;color:#3a3a3a}
.dots{left:0;top:514px;width:979px;display:flex;justify-content:center;gap:7px}
.dots b{width:10px;height:10px;border-radius:50%;background:#999;display:block}
.dots b.on{background:#333}
.rule{height:1px;background:var(--line)}

.welcome h1{font-family:"PT Sans Narrow",sans-serif;font-weight:700;font-size:24px;color:var(--red)}
.welcome{left:83px;top:576px;width:548px}
.welcome p{margin-top:10px;font-size:12px;line-height:20.4px;text-align:justify;color:#555}
.thumbs{left:84px;top:709px;display:flex;gap:8px}
.thumbs div{width:177px;height:97px}

.services{left:83px;top:835px;width:548px}
.services h2{font-family:"PT Sans Narrow",sans-serif;font-size:20px;font-weight:400;color:var(--red)}
.services p{margin-top:8px;font-size:10.6px;line-height:20.4px;color:#777}
.svc-list{left:87px;top:943px;display:grid;grid-template-columns:176px 127px 180px;row-gap:9px}
.svc-list span{font-size:10.8px;color:#777;display:flex;align-items:center;gap:8px;line-height:16px}
.svc-list span::before{content:"";width:9px;height:9px;border-radius:50%;background:#8a8a8a;box-shadow:inset 0 0 0 2px #bbb;flex:none}

.cta{left:660px;width:238px;height:59px;border-radius:3px;display:flex;align-items:center;gap:14px;padding-left:24px;font-family:"PT Sans Narrow",sans-serif;font-weight:700;color:var(--gold);font-size:22px;line-height:22px}
.cta.quote{top:581px;background:linear-gradient(#c1191e,#8f0f13);border:1px solid #6d0a0d}
.cta.brochure{top:645px;background:linear-gradient(#5a5a5a,#363636);border:1px solid #222}

.why-title{left:663px;top:722px;font-family:"PT Sans Narrow",sans-serif;font-size:20px;color:var(--red)}
.why{left:660px;top:756px;width:238px;height:252px;background:var(--panel);border-top:1px solid var(--line);border-bottom:2px solid var(--line);padding:12px 11px}
.why p{font-size:11.2px;line-height:18.7px;color:#666;text-align:justify;margin-bottom:7px}
.why p em{font-style:normal;color:var(--red-bright)}
.seal{position:absolute;left:14px;top:160px;width:75px;height:75px;border-radius:50%;background:radial-gradient(circle,#f9d463 0 55%,#e2a52a 56% 100%)}
.seal-text{position:absolute;left:101px;top:178px;font-size:16px;line-height:22px;color:#333}

.info-band{left:0;top:1038px;width:979px;height:79px;background:var(--band)}
.info{position:absolute;top:20px;display:flex;align-items:center;gap:10px;font-size:11.5px;line-height:19px;color:#777}
.info svg{flex:none}

.footer{left:0;top:1117px;width:979px;height:83px;background:var(--footer)}
.footer .links{position:absolute;left:83px;top:17px;font-size:11px;color:#bbb}
.footer .links span{padding:0 7px}
.footer .copy{position:absolute;left:83px;top:47px;font-size:11px;color:#bbb}
.social{position:absolute;right:81px;top:32px;display:flex;gap:8px}
.social b{width:21px;height:21px;border-radius:50%;background:#595959;display:block}
</style>
</head>
<body>
<div class="page">

  <div class="abs brand"><i></i><span>Tallow Creek Rails</span></div>

  <svg class="abs call-badge" viewBox="0 0 144 68" aria-label="Call us">
    <path d="M4 6 L140 2 L136 46 L96 48 L86 60 L80 49 L8 50 Z" fill="#a5141a" stroke="#7d0d11" stroke-width="2"/>
    <path d="M20 18c-2 3 0 11 6 16 5 5 11 7 14 5l2-3-5-4-3 2c-3-1-7-5-8-8l2-3-4-5z" fill="#f7b733"/>
    <text x="48" y="35" font-family="PT Sans Narrow, sans-serif" font-weight="700" font-size="22" fill="#f7b733">CALL US</text>
  </svg>

  <nav class="abs nav">
    <ul>
      <li class="active">HOME</li><li>FENCES</li><li>GATES</li><li>DECKS</li><li>DIY</li><li>CONTACT US</li>
    </ul>
    <div class="phone">03 9000 4417</div>
  </nav>

  <div class="abs slide" role="img" aria-label="Photo of a steel farm gate in a grassy paddock with grazing cattle"></div>
  <div class="abs caption">PHASELLUS ERAT FELIS, SCELERISQUE A RUTRUM VITAE, MALESUADA ID ERAT</div>
  <div class="abs dots"><b class="on"></b><b></b><b></b><b></b></div>
  <div class="abs rule" style="left:81px;top:551px;width:817px"></div>

  <section class="abs welcome">
    <h1>Welcome to Tallow Creek Rails</h1>
    <p>Donec tincidunt gravida mauris at mollis. Nulla consectetur magna et purus porttitor, nec sollicitudin felis bibendum. Pellentesque quis malesuada risus. Vivamus vehicula feugiat porttitor. Sed pellentesque ullamcorper volutpat. Praesent volutpat augue ac sapien egestas, feugiat feugiat augue convallis. Aenean neque sapien, mollis eget auctor at, lacinia nec nulla.</p>
  </section>

  <div class="abs thumbs">
    <div role="img" aria-label="Photo of a white picket fence on a lawn" style="background:linear-gradient(180deg,#7b7a5a 0%,#5d8a3a 55%,#e8e8e8 80%,#6a9a3a 100%)"></div>
    <div role="img" aria-label="Photo of a black tubular steel gate and fence" style="background:linear-gradient(180deg,#9fc06a 0%,#4c6a30 50%,#6fa23c 100%)"></div>
    <div role="img" aria-label="Photo of a pool fence beside a swimming pool" style="background:linear-gradient(160deg,#3c5a3a 0%,#7a9a6a 40%,#4aa0c8 70%,#c8c0b0 100%)"></div>
  </div>
  <div class="abs rule" style="left:86px;top:822px;width:544px"></div>

  <section class="abs services">
    <h2>Tallow Creek Rails Services</h2>
    <p>We offer a 12 month workmanshhttp://tallowcreekrails.com.au/images/site/aboutus.jpgip warranty on our fences and wll clean the site for free of any debris from the fence construction upon completion of the job. We can offer this workmanship warranty because of our work practices, these include</p>
  </section>

  <div class="abs svc-list">
    <span>Bathroom Remodeling</span><span>Tile &amp; Flooring</span><span>Genral Home Maintenance</span>
    <span>Attic &amp; Garage Finishing</span><span>Decks</span><span>Painting &amp; Wall Treatments</span>
    <span>Carpentry</span><span>Fences</span><span>Drywall Install</span>
  </div>

  <div class="abs cta quote">
    <svg width="36" height="38" viewBox="0 0 36 38" aria-hidden="true"><rect x="4" y="3" width="26" height="32" fill="#f4f4f4" stroke="#999" transform="rotate(-8 17 19)"/><g stroke="#888" stroke-width="1.5"><line x1="9" y1="12" x2="25" y2="10"/><line x1="9" y1="17" x2="25" y2="15"/><line x1="10" y1="22" x2="26" y2="20"/></g><line x1="20" y1="30" x2="33" y2="14" stroke="#e0b030" stroke-width="3"/></svg>
    <span>Instant Quote</span>
  </div>
  <div class="abs cta brochure">
    <svg width="36" height="38" viewBox="0 0 36 38" aria-hidden="true"><rect x="5" y="3" width="26" height="32" rx="2" fill="#f2f2f2"/><rect x="9" y="9" width="18" height="18" rx="2" fill="#c81e22"/></svg>
    <span>Download<br>Broucher</span>
  </div>

  <div class="abs why-title">Why Choose us?</div>
  <div class="abs why">
    <p>Nunc bibendum nunc eget nisl molestie, eu dictum dui imperdiet. Nam a augue ac ligula pulvinar rhoncus.</p>
    <p>Nunc vitae congue lorem. Nunc ut diam sed velit sollicitudin ullamcorper in a libero. Duis iaculis vulputate nisl, vel tristique sapien scelerisque eget. <em>More</em></p>
    <div class="seal"></div>
    <div class="seal-text">100% Satisfaction<br>Guarantee</div>
  </div>

  <div class="abs info-band">
    <div class="info" style="left:124px">
      <svg width="19" height="22" viewBox="0 0 19 22" aria-hidden="true"><rect x="1" y="1" width="17" height="20" fill="#999"/><rect x="5" y="5" width="9" height="14" fill="#f1f1f1"/><rect x="8" y="5" width="3" height="10" fill="#999"/></svg>
      <div>55, Building name, Street name<br>City - Zipcode</div>
    </div>
    <div class="info" style="left:390px">
      <svg width="24" height="24" viewBox="0 0 24 24" aria-hidden="true"><path d="M3 3c-3 4 2 12 8 17 3 2 6 3 9 2l2-3-5-4-3 2c-3-1-6-4-7-7l2-3-4-5z" fill="#999"/></svg>
      <div>Phone &nbsp;&nbsp;: 555.014.2286<br>Toll Free: 888.555.0193</div>
    </div>
    <div class="info" style="left:642px">
      <svg width="23" height="16" viewBox="0 0 23 16" aria-hidden="true"><rect width="23" height="16" fill="#999"/><path d="M0 0 L11.5 9 L23 0" fill="none" stroke="#f1f1f1" stroke-width="1.5"/></svg>
      <div>E-mail : info@tallowcreekrails.com.au</div>
    </div>
  </div>

  <footer class="abs footer">
    <div class="links">Privacy Policy<span>|</span>FAQ<span>|</span>Staff<span>|</span>Gallery</div>
    <div class="copy">Copyright &copy; 2013 &nbsp; Tallow Creek Rails. &nbsp; All rights reserved.</div>
    <div class="social"><b></b><b></b><b></b><b></b></div>
  </footer>

</div>
</body>
</html>
```